Business Card Design Project

I am a realtor and need a business card design that reflects the area in which I work which is West Vancouver, BC, Canada. I am looking for a backdrop of a waterfront luxury home with pool on top of which I can insert my personal photo. The colors would be blue of course, for the water and pool and possibly white and brown for the home. The card should state in bold, 'Lorna Pelcroft Real Estate'. It also needs to say in smaller print 'Meridot Calloway Realty'. I would need to include my contact information. I would also like to be able to use the same design as a header in my real estate newspaper ads.

Target Market(s)

sellers and buyers of luxury real estate

Industry/Entity Type

Real Estate

Requirements
Must have
• Must include my personal photo and contact information

cell 604 555-0173
email lornap@quellnet.ca
website lornapelcroft.com

Must also include 'Meridot Calloway Realty' in smaller print

```html
<!DOCTYPE html>
<html lang="en">
<head>
<meta charset="utf-8">
<title>Lorna Pelcroft Real Estate — Business Card</title>
<link href="https://fonts.googleapis.com/css2?family=Tinos:wght@400&family=Open+Sans:wght@400;600&display=swap" rel="stylesheet">
<style>
  :root {
    --page: #e6e7ea;
    --card-white: #ffffff;
    --card-grey: #e9e9ea;
    --navy: #14117a;
    --brand-blue: #24308f;
    --brown: #7a4212;
    --text-grey: #6f7278;
    --icon-blue: #2d4fa0;
    --back-light: #5d9bd0;
    --back-dark: #2b5f96;
    --photo-light: #eeeae6;
    --photo-warm: #d6b894;
  }
  * { box-sizing: border-box; margin: 0; padding: 0; }
  html, body { width: 1200px; height: 899px; overflow: hidden; }
  body { background: var(--page); position: relative; font-family: "Open Sans", sans-serif; }

  .card {
    position: absolute;
    left: 250px;
    width: 700px;
    height: 380px;
    overflow: hidden;
    box-shadow: 0 6px 18px rgba(0,0,0,.22);
  }
  .card--back {
    top: 45px;
    background: radial-gradient(ellipse at 50% 42%, var(--back-light) 0%, var(--back-dark) 70%);
  }
  .card--front {
    top: 470px;
    background: linear-gradient(90deg, var(--card-grey) 0%, var(--card-white) 45%, var(--card-white) 100%);
  }

  .brand { position: absolute; font-family: "Tinos", serif; font-weight: 400; }
  .brand__name { display: block; font-size: 22px; letter-spacing: .5px; text-transform: uppercase; }
  .brand__sub { display: block; font-size: 11px; letter-spacing: .3px; }

  .card--back .brand { left: 0; right: 0; top: 168px; text-align: center; color: #cfe0f1; }
  .card--back .brand__name { font-size: 20px; }
  .card--back .brand__sub { margin-top: 4px; color: #cfe0f1; }

  .card--front .brand { left: 48px; top: 96px; color: var(--brand-blue); display: flex; align-items: flex-start; gap: 10px; }
  .brand__mark { width: 14px; height: 14px; background: var(--icon-blue); margin-top: 6px; }
  .card--front .brand__sub { margin-top: 3px; color: var(--text-grey); }

  .contact { position: absolute; left: 60px; top: 230px; list-style: none; color: var(--text-grey); font-size: 15px; letter-spacing: 1px; }
  .contact li { display: flex; align-items: center; gap: 16px; height: 26px; }
  .contact svg { width: 16px; height: 16px; fill: none; stroke: var(--icon-blue); stroke-width: 1.6; }

  .card__art { position: absolute; top: 0; left: 0; width: 700px; height: 380px; }
</style>
</head>
<body>

<section class="card card--back" aria-label="Card back">
  <div class="brand">
    <span class="brand__name">Lorna Pelcroft Real Estate</span>
    <span class="brand__sub">Meridot Calloway Realty</span>
  </div>
</section>

<section class="card card--front" aria-label="Card front">
  <svg class="card__art" viewBox="0 0 700 380">
    <defs>
      <linearGradient id="photoTone" x1="0" y1="0" x2="1" y2="1">
        <stop offset="0" stop-color="var(--photo-light)"/>
        <stop offset="1" stop-color="var(--photo-warm)"/>
      </linearGradient>
    </defs>
    <path d="M375,0 L565,0 Q650,190 580,380 L375,380 Z" fill="url(#photoTone)" role="img" aria-label="Portrait photo of the realtor"/>
    <path d="M585,15 Q670,190 600,380 L635,380 Q705,190 610,0 Z" fill="var(--brown)"/>
    <path d="M620,0 L700,0 L700,380 L645,380 Q720,190 620,0 Z" fill="var(--navy)"/>
  </svg>

  <div class="brand">
    <span class="brand__mark"></span>
    <span>
      <span class="brand__name">Lorna Pelcroft Real Estate</span>
      <span class="brand__sub">Meridot Calloway Realty</span>
    </span>
  </div>

  <ul class="contact">
    <li>
      <svg viewBox="0 0 16 16"><rect x="4" y="1" width="8" height="14" rx="1.5"/><line x1="7" y1="12.5" x2="9" y2="12.5"/></svg>
      <span>604 555-0173</span>
    </li>
    <li>
      <svg viewBox="0 0 16 16"><rect x="1" y="3" width="14" height="10" rx="1"/><path d="M1,4 L8,9 L15,4"/></svg>
      <span>lornap@quellnet.ca</span>
    </li>
    <li>
      <svg viewBox="0 0 16 16"><circle cx="8" cy="8" r="6.5"/><ellipse cx="8" cy="8" rx="3" ry="6.5"/><line x1="1.5" y1="8" x2="14.5" y2="8"/></svg>
      <span>www.lornapelcroft.com</span>
    </li>
  </ul>
</section>

</body>
</html>
```